Business Card Design Project

A business card for a new company in Ontario Canada called Build for Growth. It is a consulting company which uses Brixo as the medium for facilitation.

The target market is for senior leaders in healthcare and social services.

Industry/Entity Type

Healthcare

Requirements
Must have
• The name Build For Growth
Dana Montreuil RRT, B Ed (AD ed).
Tacticraft Facililitator (R)

Tag Line
Engaging Transforming and Innovative
The attached logo

danamontreuil@examplemail.com
416-555-0147
Should not have
• Lime green
Times New Roman or Arial font
Do not include Brixo bricks on the card.

```html
<!DOCTYPE html>
<html lang="en">
<head>
<meta charset="utf-8">
<title>Build For Growth – Business Card</title>
<link rel="stylesheet" href="https://fonts.googleapis.com/css2?family=Alegreya:wght@400;500;700&family=Alegreya+SC:wght@500;700&family=Open+Sans:wght@600;700&display=swap">
<style>
  :root {
    --page-bg: #ececec;
    --card-bg: #ffffff;
    --purple: #4b0a7a;
    --blue: #3f9ed3;
    --grey-text: #8c8c8c;
    --edge-line: #3f9ed3;
  }
  * { margin: 0; padding: 0; box-sizing: border-box; }
  html, body {
    width: 1200px;
    height: 900px;
    overflow: hidden;
    background: var(--page-bg);
  }
  .canvas {
    position: relative;
    width: 1200px;
    height: 900px;
  }
  .business-card {
    position: absolute;
    left: 236px;
    top: 220px;
    width: 748px;
    height: 456px;
    background: var(--card-bg);
    overflow: hidden;
  }
  .edge-waves {
    position: absolute;
    inset: 0;
    width: 100%;
    height: 100%;
  }
  .edge-wave { fill: var(--purple); stroke: var(--edge-line); stroke-width: 2; }

  .brand {
    position: absolute;
    left: 0;
    right: 0;
    top: 140px;
    display: flex;
    align-items: center;
    justify-content: center;
    gap: 14px;
  }
  .brand-dot {
    width: 22px;
    height: 22px;
    border-radius: 50%;
    background: var(--purple);
  }
  .brand-name {
    font-family: "Alegreya", Georgia, serif;
    font-weight: 500;
    font-size: 34px;
    color: var(--purple);
    letter-spacing: 0.5px;
  }
  .tagline {
    position: absolute;
    left: 0;
    right: 0;
    top: 206px;
    text-align: center;
    font-family: "Alegreya", Georgia, serif;
    font-size: 22px;
    color: var(--grey-text);
  }
  .person-name {
    position: absolute;
    left: 0;
    right: 0;
    top: 284px;
    text-align: center;
    font-family: "Alegreya SC", Georgia, serif;
    font-weight: 700;
    font-size: 36px;
    color: var(--purple);
    letter-spacing: 1px;
  }
  .credentials {
    font-family: "Alegreya", Georgia, serif;
    font-weight: 700;
    font-size: 15px;
    letter-spacing: 0;
    margin-left: 6px;
  }
  .role {
    position: absolute;
    left: 0;
    right: 0;
    top: 334px;
    text-align: center;
    font-family: "Open Sans", Helvetica, sans-serif;
    font-weight: 600;
    font-size: 23px;
    color: var(--blue);
  }
  .contact-list {
    position: absolute;
    left: 104px;
    top: 384px;
    display: flex;
    gap: 44px;
    list-style: none;
    font-family: "Open Sans", Helvetica, sans-serif;
    font-weight: 700;
    font-size: 19px;
    color: var(--blue);
  }
  .contact-item {
    display: flex;
    align-items: center;
    gap: 16px;
  }
  .contact-marker {
    width: 20px;
    height: 20px;
    background: var(--purple);
  }
</style>
</head>
<body>
<main class="canvas">
  <article class="business-card">
    <svg class="edge-waves" viewBox="0 0 748 456" aria-hidden="true">
      <path class="edge-wave" d="M-2 -2 H24 C50 70 48 150 24 232 C6 300 10 390 38 458 H-2 Z"/>
      <path class="edge-wave" d="M750 -2 H722 C698 80 700 170 722 250 C740 320 736 400 712 458 H750 Z"/>
    </svg>

    <div class="brand">
      <span class="brand-dot"></span>
      <span class="brand-name">Build For Growth</span>
    </div>
    <p class="tagline">Engaging Transforming and Innovative</p>

    <h1 class="person-name">Dana Montreuil<span class="credentials">RRT, B Ed (AD ed)</span></h1>
    <p class="role">Tacticraft Facilitator (R)</p>

    <ul class="contact-list">
      <li class="contact-item"><span class="contact-marker"></span>416-555-0147</li>
      <li class="contact-item"><span class="contact-marker"></span>danamontreuil@examplemail.com</li>
    </ul>
  </article>
</main>
</body>
</html>
```